Brochure Design Project

Please design a corporate brochure for my business "Corvin Asbestos & Safety"

Specs:-
- A4 flat size, three panel front, three panel back, roll-folded to DL
- Portrait orientation
- Full colour
Updates

Please don't forget to send in your designs. I believe the competition ends in a few hours. Thank you!

Target Market(s)

Business owners, commercial/industrial building owners, real estate property managers, strata managers

Industry/Entity Type

Business

Requirements
Must have
• - Professional / modern but serious as the content is important
- Cover page in particular must stand out so it will be noticeable if sitting on someone's desk
- Good use of whitespace and not too crowded
- Heading highlighted in warm/hot colour i.e. burnt orange, all other text in black
- Font Georgia 11pt
Nice to have
• - I have uploaded our letterhead source files too - please weave in the theme/look and feel of the letterhead into the brochure if possible.

```html
<!DOCTYPE html>
<html lang="en">
<head>
<meta charset="utf-8">
<title>Corvin Asbestos &amp; Safety – Brochure Inside</title>
<link href="https://fonts.googleapis.com/css2?family=Anton&family=Arimo:ital,wght@0,400;0,700;1,400;1,700&display=swap" rel="stylesheet">
<style>
  :root {
    --backdrop: #000000;
    --paper: #ffffff;
    --navy: #16187a;
    --lime: #7ed321;
    --alert: #d2401a;
    --ink: #1a1a1a;
    --fold: #9aa0b5;
    --warn-yellow: #ffec00;
  }
  * { margin: 0; padding: 0; box-sizing: border-box; }
  html, body {
    width: 1200px; height: 927px; overflow: hidden;
    background: var(--backdrop);
  }
  .brochure {
    position: absolute; left: 126px; top: 75px;
    width: 951px; height: 750px;
    background: var(--paper);
    font-family: "Arimo", Arial, sans-serif;
    color: var(--ink);
    overflow: hidden;
  }
  .band { position: absolute; left: 0; width: 951px; }
  .band--top { top: 0; height: 52px; }
  .band--bottom { bottom: 0; height: 62px; }
  .fold-line {
    position: absolute; top: 52px; bottom: 62px; width: 0;
    border-left: 1px dashed var(--fold);
  }
  .fold-line--one { left: 310px; }
  .fold-line--two { left: 621px; }

  .panel-cover {
    position: absolute; left: 20px; top: 62px; width: 270px;
  }
  .danger-title {
    font-family: "Anton", "Arial Narrow", sans-serif;
    font-size: 46px; line-height: 46px; text-align: center;
    letter-spacing: 0.5px; color: #000;
    padding-left: 24px;
  }
  .warning-sign { display: block; margin: 14px 0 0 72px; }
  .alert-heading {
    font-weight: 700; font-style: italic;
    color: var(--alert);
    text-shadow: 1px 1px 0 rgba(0,0,0,0.35);
  }
  .panel-cover .alert-heading { font-size: 16px; margin-top: 22px; }
  .cover-copy {
    font-style: italic; font-size: 14px; line-height: 18.5px;
    text-align: justify; margin-top: 12px;
  }
  .cover-copy + .cover-copy { margin-top: 18px; }
  .brand-mark {
    display: flex; align-items: center; gap: 10px;
    margin: 32px 0 0 44px;
  }
  .brand-mark__square { width: 26px; height: 26px; background: var(--lime); }
  .brand-mark__name {
    font-size: 19px; font-weight: 700; color: var(--navy); line-height: 22px;
  }

  .panel-compliance {
    position: absolute; left: 339px; top: 63px; width: 598px;
    font-size: 13.6px; line-height: 17.5px;
  }
  .panel-compliance .alert-heading { font-size: 17px; line-height: 18px; }
  .panel-compliance p { margin-top: 12px; }
  .panel-compliance h2.alert-heading { margin-top: 18px; }
  .list-title { font-weight: 700; font-style: italic; margin-top: 12px; }
  .duty-list { list-style: none; padding-left: 12px; }
  .duty-list li { padding-left: 10px; text-indent: -10px; }
  .duty-list li::before { content: "•"; display: inline-block; width: 10px; text-indent: 0; }

  .contact-strip {
    position: absolute; left: 339px; top: 680px;
    display: flex; gap: 8px; font-size: 8px; line-height: 11px;
  }
  .contact-strip__col { padding-left: 5px; border-left: 1px solid var(--lime); }
</style>
</head>
<body>
<main class="brochure">
  <svg class="band band--top" viewBox="0 0 951 52" aria-hidden="true">
    <polygon points="300,0 951,0 951,34 318,34" fill="var(--navy)"/>
    <polygon points="0,0 290,0 318,50 0,50" fill="var(--lime)"/>
  </svg>
  <svg class="band band--bottom" viewBox="0 0 951 62" aria-hidden="true">
    <polygon points="0,14 951,14 951,62 0,62" fill="var(--navy)"/>
    <polygon points="680,0 951,0 951,62 650,62" fill="var(--lime)"/>
  </svg>
  <div class="fold-line fold-line--one"></div>
  <div class="fold-line fold-line--two"></div>

  <section class="panel-cover">
    <h1 class="danger-title">DANGER<br>ASBESTOS</h1>
    <svg class="warning-sign" width="134" height="128" viewBox="0 0 134 128" role="img" aria-label="Warning sign">
      <polygon points="67,4 130,123 4,123" fill="var(--warn-yellow)" stroke="#000" stroke-width="7" stroke-linejoin="round"/>
      <polygon points="59,42 75,42 71,92 63,92" fill="#000"/>
      <circle cx="67" cy="106" r="8" fill="#000"/>
    </svg>
    <h2 class="alert-heading">Why is Asbestos so dangerous?</h2>
    <p class="cover-copy">Asbestos is a hazardous substance that poses a risk to health by inhalation if the asbestos fibres become airborne. Exposure to these fibres is known to cause mesothelioma, asbestosis and lung cancer.</p>
    <p class="cover-copy">Australia had the highest per capita use of asbestos in the world in the 1950s and it is not surprising that it has the world’s highest incidence of asbestos related cancer. Asbestos has caused a significant death toll and much suffering in Australia, and the impact of asbestos-related diseases is expected to peak in 2020.</p>
    <div class="brand-mark">
      <span class="brand-mark__square"></span>
      <span class="brand-mark__name">Corvin Asbestos &amp; Safety</span>
    </div>
  </section>

  <section class="panel-compliance">
    <h2 class="alert-heading">Are you compliant with current Work Health and Safety (WHS) Legislation regarding Asbestos?</h2>
    <p>The Work Health and Safety (WHS) Regulation (2011) and its associated Code of Practice – How to Manage and Control Asbestos in the Workplace requires that all non-domestic buildings constructed prior to 31st December 2003 must have a compliant Asbestos Register and Asbestos Management Plan.</p>
    <p>This covers all buildings in which people work – commercial, retail, industrial, community, educational, healthcare, accommodation and some strata developments.</p>
    <p>Fines of up to $30,000 apply for non-compliance.</p>
    <h2 class="alert-heading">What is an Asbestos Register and Management Plan?</h2>
    <h3 class="list-title">An Asbestos Register must:</h3>
    <ul class="duty-list">
      <li>Record any asbestos that has been identified or is assumed to be present at the workplace.</li>
      <li>Record the date when the asbestos was identified.</li>
      <li>Record the location, type and condition of the asbestos.</li>
      <li>Be maintained to ensure up-to-date information.</li>
      <li>State if no asbestos has been identified.</li>
      <li>Be given to the person conducting a business or undertaking (PCBU) when there is a change of management or controller of the workplace.</li>
    </ul>
    <h3 class="list-title">The Asbestos Management Plan must:</h3>
    <ul class="duty-list">
      <li>Identify the location of asbestos and any naturally occurring asbestos.</li>
      <li>Include decisions, and reasons for decisions, about the management of asbestos at the workplace for example safe work procedures and control measures.</li>
      <li>Outline procedures for incidents and emergencies involving asbestos, including who is responsible.</li>
      <li>Be maintained with up-to-date information.</li>
      <li>Be reviewed at least every five years or when requested by a health and safety representative (HSR) or when asbestos is removed, disturbed, sealed or enclosed, or when changes to a control measure are made or when the plan is no longer adequate.</li>
    </ul>
  </section>

  <footer class="contact-strip">
    <div class="contact-strip__col">(02) 5550 1670<br>(02) 5550 7882</div>
    <div class="contact-strip__col">Suite 3, 18 Marlin St<br>Harbourvale, NSW 2099</div>
    <div class="contact-strip__col">info@corvinsafety.com.au<br>www.corvinsafety.com.au</div>
  </footer>
</main>
</body>
</html>
```